Manuka honey wholesales and exports

We need business cards for our honey distribution company based in New Zealand. We supply shops locally and export Manuka honey around the world.
We deal with a very high quality and 100% natural product that can be used for medical, general health as well as food. We are looking business cards that show our honey products are of a high quality with a modern look.

Target Market(s)

Health and medical retailers and importers

Industry/Entity Type

Wholesale

Contact Information for Business Card

Kestrel Hive NZ Limited

www.kestrelhivenz.com

Gareth Moffat

M +64 213958264

E kestrelhivenz@mailbox-example.com

PO Box 47-518
Takapuna
North Shore
Auckland
New Zealand

Font styles to use
Serif

Requirements
Must have
• (Kestrel Hive NZ Limited) with some artwork on one side and all details on the other side.
Nice to have
• I have seen a very simple card with large yellow and black stripes on one side with a company name.. looked clean and simple so something similar or just let the creative beast inside you take over and we will see what you can come up with.

```html
<!DOCTYPE html>
<html lang="en">
<head>
<meta charset="utf-8">
<title>Kestrel Hive NZ Limited – Business Cards</title>
<link href="https://fonts.googleapis.com/css2?family=Questrial&family=Open+Sans:wght@300;400;700&display=swap" rel="stylesheet">
<style>
  :root {
    --bg: #e1e1e1;
    --card-dark: #2b2b2b;
    --card-mid: #363636;
    --honey: #f0d90f;
    --text-light: #d8d8d8;
    --text-muted: #b9b9b9;
    --white: #ffffff;
  }
  * { box-sizing: border-box; margin: 0; padding: 0; }
  html, body {
    width: 1200px; height: 1000px; overflow: hidden;
    background: var(--bg);
    font-family: "Open Sans", Arial, sans-serif;
  }
  .stage { position: relative; width: 1200px; height: 1000px; }

  .card {
    position: absolute;
    width: 560px; height: 320px;
    border-radius: 26px;
    overflow: hidden;
    background: radial-gradient(ellipse at 55% 35%, var(--card-mid) 0%, var(--card-dark) 70%);
    box-shadow: 0 14px 30px rgba(0,0,0,0.28);
  }
  .card-front { left: 150px; top: 130px; }
  .card-back  { left: 490px; top: 530px; }

  /* Front */
  .world-map-area {
    position: absolute; left: 40px; top: 30px; width: 480px; height: 260px;
    border-radius: 40%;
    background: radial-gradient(ellipse at center, rgba(255,255,255,0.06) 0%, rgba(255,255,255,0.02) 55%, rgba(255,255,255,0) 75%);
  }
  .front-brand {
    position: absolute; left: 0; right: 0; top: 128px;
    text-align: center;
  }
  .brand-mark {
    display: inline-flex; align-items: center; gap: 10px;
    font-family: "Questrial", Arial, sans-serif;
    font-weight: 400;
    color: var(--honey);
    white-space: nowrap;
  }
  .brand-dot {
    width: 16px; height: 16px; border-radius: 50%;
    background: var(--honey);
    flex: none;
  }
  .front-brand .brand-mark { font-size: 28px; }
  .front-url {
    margin-top: 22px;
    font-size: 13px; letter-spacing: 4px;
    color: var(--honey);
  }

  /* Back */
  .back-title {
    position: absolute; left: 34px; top: 44px;
    font-family: "Questrial", Arial, sans-serif;
    font-weight: 400;
    font-size: 32px; line-height: 40px;
    color: var(--honey);
    white-space: nowrap;
  }
  .back-corner-brand {
    position: absolute; right: 32px; top: 124px;
  }
  .back-corner-brand .brand-mark { font-size: 17px; gap: 8px; }
  .back-corner-brand .brand-dot { width: 12px; height: 12px; }

  .name-marker {
    position: absolute; left: 0; top: 141px;
    width: 16px; height: 18px; background: var(--honey);
  }
  .person-name {
    position: absolute; left: 36px; top: 136px;
    font-weight: 700; font-size: 21px; line-height: 28px; letter-spacing: 1px;
    color: var(--white); text-transform: uppercase;
  }
  .address {
    position: absolute; left: 36px; top: 174px;
    font-size: 12.5px; line-height: 17px; font-weight: 300;
    color: var(--text-muted);
  }
  .contact-list {
    position: absolute; left: 36px; top: 220px;
    list-style: none;
  }
  .contact-list li {
    display: flex; align-items: center; gap: 10px;
    font-size: 12.5px; font-weight: 300; color: var(--text-light);
    height: 22px;
  }
  .contact-icon { width: 16px; height: 16px; flex: none; }
  .honey-band {
    position: absolute; left: 0; right: 0; bottom: 0; height: 14px;
    background: linear-gradient(90deg, #e3c80c, var(--honey));
  }
</style>
</head>
<body>
<main class="stage">

  <section class="card card-front" aria-label="Business card front">
    <div class="world-map-area" role="img" aria-label="Faint world map in the card background"></div>
    <div class="front-brand">
      <div class="brand-mark"><span class="brand-dot"></span><span>Kestrel Hive NZ Limited</span></div>
      <p class="front-url">www.kestrelhivenz.com</p>
    </div>
  </section>

  <section class="card card-back" aria-label="Business card back">
    <h1 class="back-title">Kestrel Hive NZ Limited</h1>
    <div class="back-corner-brand">
      <div class="brand-mark"><span class="brand-dot"></span><span>Kestrel Hive NZ Limited</span></div>
    </div>

    <span class="name-marker"></span>
    <h2 class="person-name">Gareth Moffat</h2>
    <p class="address">PO Box 47-518 Takapuna North Shore,<br>Auckland New Zealand</p>

    <ul class="contact-list">
      <li>
        <svg class="contact-icon" viewBox="0 0 16 16" aria-hidden="true">
          <circle cx="8" cy="8" r="8" fill="#f0d90f"/>
          <path d="M5 4.5c.5-.4 1-.3 1.3.2l.6 1.1c.2.4.1.8-.2 1l-.4.3c.4.9 1.1 1.6 2 2l.3-.4c.3-.3.7-.4 1-.2l1.1.6c.5.3.6.8.2 1.3-.6.8-1.6 1-2.5.5C6.6 10 5.5 8.9 4.7 7.1c-.4-.9-.3-1.9.3-2.6z" fill="#2b2b2b"/>
        </svg>
        <span>+64 213 958 264</span>
      </li>
      <li>
        <svg class="contact-icon" viewBox="0 0 16 16" aria-hidden="true">
          <circle cx="8" cy="8" r="8" fill="#f0d90f"/>
          <rect x="4" y="5.2" width="8" height="5.6" fill="none" stroke="#2b2b2b" stroke-width="1.1"/>
          <path d="M4 5.4l4 3 4-3" fill="none" stroke="#2b2b2b" stroke-width="1.1"/>
        </svg>
        <span>kestrelhivenz@mailbox-example.com</span>
      </li>
      <li>
        <svg class="contact-icon" viewBox="0 0 16 16" aria-hidden="true">
          <circle cx="8" cy="8" r="8" fill="#f0d90f"/>
          <circle cx="8" cy="8" r="4" fill="none" stroke="#2b2b2b" stroke-width="1"/>
          <ellipse cx="8" cy="8" rx="1.8" ry="4" fill="none" stroke="#2b2b2b" stroke-width="1"/>
          <line x1="4" y1="8" x2="12" y2="8" stroke="#2b2b2b" stroke-width="1"/>
        </svg>
        <span>www.kestrelhivenz.com</span>
      </li>
    </ul>

    <div class="honey-band"></div>
  </section>

</main>
</body>
</html>
```